Vell Partners Building Business Cards

We need a business card that reflects our business as "Solar Experts" in San Diego. Browse our website www.vellpartners.example our License needs to be displayed as "CSLB# 4718392" our phone number is (619) 555-0147

Save thousands on your electric bills and increase the value of your home while helping to protect the environment. Our solar installation experts will help you design the system that's right for you, using only the highest quality equipment that will look great and give you ideal performance. Our goal is to make you energy independent, and get your electric bill to 0.

Tobias Wrenfield
(619) 555-0147
tobias@vellpartners.example

Target Market(s)

Home owners in san diego looking for solar

Industry/Entity Type

Solar Energy

Contact Information for Business Card

Tobias Wrenfield
(619) 555-0147
tobias@vellpartners.example

Font styles to use
Other font styles liked:
• Use our logo font

Requirements
Must have
• License needs to be displayed as "CSLB# 4718392" our phone number is (619) 555-0147
Nice to have
• Real images of rooftop home solar in san diego
Should not have
• our business address

```html
<!DOCTYPE html>
<html lang="en">
<head>
<meta charset="utf-8">
<title>Vell Partners Building — Business Cards</title>
<link href="https://fonts.googleapis.com/css2?family=Montserrat:wght@500;600;700&display=swap" rel="stylesheet">
<style>
  :root {
    --backdrop: #e3e6e6;
    --card-dark: #15171f;
    --accent: #f5a20a;
    --accent-shade: #b87400;
    --card-light: #f6f6f6;
    --brand-blue: #2443b8;
    --ink: #1c1c1c;
    --ink-soft: #444;
  }
  * { margin: 0; padding: 0; box-sizing: border-box; }
  html, body {
    width: 1200px; height: 686px; overflow: hidden;
    background: var(--backdrop);
    font-family: "Montserrat", Arial, sans-serif;
  }
  .canvas { position: relative; width: 1200px; height: 686px; }

  .card {
    position: absolute; top: 200px;
    width: 500px; height: 286px;
    overflow: hidden;
    box-shadow: 0 10px 24px rgba(0,0,0,.12);
  }
  .card--front { left: 60px; background: var(--card-dark); }
  .card--back { left: 640px; background: var(--card-light); }

  .band {
    position: absolute; left: 0; right: 0; height: 34px;
    background: var(--accent);
  }
  .band--top { top: 52px; }
  .band--bottom { top: 204px; }

  .brand {
    position: absolute; display: flex; align-items: center; gap: 10px;
    color: var(--brand-blue); font-weight: 700; white-space: nowrap;
  }
  .brand__dot {
    border-radius: 50%; background: var(--accent); flex: none;
  }
  .card--front .brand { left: 0; right: 0; top: 126px; justify-content: center; font-size: 27px; }
  .card--front .brand__dot { width: 22px; height: 22px; }

  .back-shapes { position: absolute; inset: 0; }

  .card--back .brand { left: 22px; top: 122px; font-size: 19px; }
  .card--back .brand__dot { width: 16px; height: 16px; }

  .name-tab {
    position: absolute; left: 270px; right: 0; top: 62px; height: 34px;
    background: var(--accent);
    display: flex; align-items: center; justify-content: center;
    font-size: 18px; font-weight: 600; color: var(--ink);
  }

  .contact {
    position: absolute; left: 316px; display: flex; align-items: center; gap: 10px;
    font-size: 8px; line-height: 1.35; color: var(--ink-soft);
  }
  .contact--phone { top: 140px; }
  .contact--email { top: 182px; }
  .contact__icon { width: 22px; height: 22px; flex: none; }
  .contact__label { font-weight: 600; color: var(--ink); }

  .license {
    position: absolute; right: 22px; bottom: 24px;
    font-size: 7px; font-weight: 600; color: var(--ink);
  }
</style>
</head>
<body>
<main class="canvas">

  <section class="card card--front" aria-label="Business card front">
    <div class="band band--top"></div>
    <div class="band band--bottom"></div>
    <div class="brand"><span class="brand__dot"></span>Vell Partners Building</div>
  </section>

  <section class="card card--back" aria-label="Business card back">
    <svg class="back-shapes" viewBox="0 0 500 286" preserveAspectRatio="none" aria-hidden="true">
      <polygon points="0,0 312,0 250,286 0,286" fill="#15171f"/>
      <polygon points="270,96 290,96 290,110" fill="#b87400"/>
      <polygon points="0,244 62,244 52,268 0,268" fill="#f5a20a"/>
    </svg>

    <div class="brand"><span class="brand__dot"></span>Vell Partners Building</div>

    <div class="name-tab">Tobias Wrenfield</div>

    <div class="contact contact--phone">
      <svg class="contact__icon" viewBox="0 0 22 22" aria-hidden="true">
        <polygon points="11,1 20,6 20,16 11,21 2,16 2,6" fill="#f5a20a"/>
        <path d="M7.5 6.5c.6-.6 1.3-.5 1.7.1l.8 1.3c.3.5.2 1-.2 1.4l-.5.5c.6 1.2 1.5 2.1 2.7 2.7l.5-.5c.4-.4.9-.5 1.4-.2l1.3.8c.6.4.7 1.1.1 1.7l-.7.7c-.7.7-2 .6-3.6-.4-1.5-.9-2.8-2.2-3.7-3.7-1-1.6-1.1-2.9-.4-3.6z" fill="#fff"/>
      </svg>
      <div><div class="contact__label">Phone number</div><div>(619) 555-0147</div></div>
    </div>

    <div class="contact contact--email">
      <svg class="contact__icon" viewBox="0 0 22 22" aria-hidden="true">
        <polygon points="11,1 20,6 20,16 11,21 2,16 2,6" fill="#f5a20a"/>
        <circle cx="11" cy="11" r="4.5" fill="none" stroke="#fff" stroke-width="1.4"/>
        <circle cx="11" cy="11" r="1.6" fill="#fff"/>
      </svg>
      <div><div class="contact__label">Contact us</div><div>tobias@vellpartners.example</div></div>
    </div>

    <div class="license">CSLB# 4718392</div>
  </section>

</main>
</body>
</html>
```